Price Calculator as Responsive Web App to support Sales People

We need to build a simple micro web app to support sales people in making quotes. We already have a backend that can take a number of parameters and create a quote. We need put a responsive web app on top of this so that our people on the road can easily do their price simulations.

We need two pages. One for the input and another for the results. No menus, navigations, etc. It is 6 different inputs as shown with boxes in the sketch. They don't need to be boxed, but some of them have a bit of instruction text that clearly need to belong to the input.

This needs to be responsive, but first and foremost designed for smartphones. I have included a background gradient that we would like to use -- or a variant of it. We expect this to be delivered as HTML/CSS + images so that we can quickly write a few pieces of JavaScript ourselves to wire it up to our price simulator.

Industry/Entity Type

Information Technology

Coding

Coded - Design and coding required

Number of Pages Required

2 page

Font styles to use
Sans Serif

Requirements
Must have
• Responsive design
• Easy to wire up JavaScript to the HTML/CSS
Nice to have
• Some quick way to pick number of months. +/- buttons to add remove a year or 3 months. Same thing with number of items. Add 10 or 5 quickly.
• Maybe some parallax effect while scrolling as long as it is not distracting.
Should not have
• Toolbars, Menus, Navigations, Banners, etc. This is just a single micro app.

```html
<!DOCTYPE html>
<html lang="en">
<head>
<meta charset="utf-8">
<title>Engine Power Form</title>
<link rel="stylesheet" href="https://fonts.googleapis.com/css2?family=Oswald:wght@400;500&family=Jost:wght@400;500&family=Lato:wght@700&display=swap">
<style>
:root{
  --bg-top:#21546a;
  --bg-mid:#1c3b4e;
  --bg-bottom:#1e2530;
  --panel:rgba(150,175,190,0.42);
  --panel-line:rgba(255,255,255,0.14);
  --step-border:rgba(255,255,255,0.12);
  --value-bg:#344d5a;
  --selected:rgba(45,60,75,0.62);
  --text:#ffffff;
  --submit:#2f7fca;
  --footer:#000000;
}
*{box-sizing:border-box;margin:0;padding:0}
html,body{width:1158px;height:1200px;overflow:hidden}
body{
  position:relative;
  background:radial-gradient(ellipse at 50% 0%,var(--bg-top) 0%,var(--bg-mid) 45%,var(--bg-bottom) 100%);
  color:var(--text);
  font-family:"Jost",sans-serif;
}
.page-title{
  position:absolute;left:0;right:0;top:18px;text-align:center;
  font-family:"Oswald",sans-serif;font-weight:400;font-size:37px;letter-spacing:.5px;
}
.stepper,.panel{position:absolute;left:155px;width:847px;background:var(--panel)}
.stepper{height:58px}
.stepper-label{
  position:absolute;left:23px;top:0;line-height:58px;
  font-family:"Oswald",sans-serif;font-size:25px;
}
.stepper-divider{position:absolute;left:189px;top:0;bottom:0;width:1px;background:var(--panel-line)}
.step-btn,.step-value{
  position:absolute;top:6px;width:58px;height:46px;
  display:flex;align-items:center;justify-content:center;
  font-size:22px;border:1px solid var(--step-border);
}
.step-value{background:var(--value-bg);border-color:rgba(255,255,255,.2)}
.step-unit{position:absolute;left:511px;top:0;line-height:58px;font-size:17px;font-weight:500}
.panel-title{
  position:absolute;left:23px;top:12px;
  font-family:"Oswald",sans-serif;font-size:25px;
}
.panel-divider{position:absolute;left:23px;right:20px;height:1px;background:var(--panel-line)}
.option{position:absolute;display:flex;align-items:center;font-size:17px;height:34px}
.option.is-selected{background:var(--selected)}
.radio{
  position:absolute;width:21px;height:21px;border:1.5px solid #fff;border-radius:50%;
}
.option.is-selected .radio::after{
  content:"";position:absolute;left:4px;top:4px;width:10px;height:10px;border-radius:50%;background:#fff;
}
.option-text{position:absolute;white-space:nowrap}
.notice{position:absolute;left:29px;top:250px;font-size:13px}
.notice b{font-weight:500}
.submit{
  position:absolute;left:155px;top:1070px;width:145px;height:50px;
  background:var(--submit);color:#fff;border:0;
  font-family:"Lato",sans-serif;font-weight:700;font-size:20px;
  display:flex;align-items:center;gap:10px;padding-left:20px;
}
.site-footer{
  position:absolute;left:0;right:0;top:1146px;height:54px;background:var(--footer);
  display:flex;align-items:center;justify-content:center;
  font-family:"Lato",sans-serif;font-weight:400;font-size:11.5px;
}
</style>
</head>
<body>
<h1 class="page-title">ENGINE POWER FORM</h1>

<section class="stepper" style="top:92px">
  <span class="stepper-label">Duration</span>
  <span class="stepper-divider"></span>
  <span class="step-btn" style="left:253px">-1</span>
  <span class="step-btn" style="left:329px">-12</span>
  <span class="step-value" style="left:439px">24</span>
  <span class="step-unit">MONTH</span>
  <span class="step-btn" style="left:605px">+1</span>
  <span class="step-btn" style="left:681px">+12</span>
</section>

<section class="stepper" style="top:174px">
  <span class="stepper-label">Count</span>
  <span class="stepper-divider"></span>
  <span class="step-btn" style="left:253px">-1</span>
  <span class="step-btn" style="left:329px">-10</span>
  <span class="step-value" style="left:439px">100</span>
  <span class="step-unit">ITEMS</span>
  <span class="step-btn" style="left:605px">+1</span>
  <span class="step-btn" style="left:681px">+10</span>
</section>

<section class="panel" style="top:258px;height:281px">
  <h2 class="panel-title">Engine Power (Beyond Standard)</h2>
  <span class="panel-divider" style="top:60px"></span>
  <div class="option" style="left:0;top:79px;width:847px">
    <span class="radio" style="left:25px"></span><span class="option-text" style="left:63px">360 $ / Year &nbsp;- &nbsp;Bounce Power</span>
  </div>
  <div class="option is-selected" style="left:17px;top:120px;width:811px;height:41px">
    <span class="radio" style="left:8px"></span><span class="option-text" style="left:46px">600 $ / Year &nbsp;- &nbsp;Silver Power</span>
  </div>
  <div class="option" style="left:0;top:166px;width:847px">
    <span class="radio" style="left:25px"></span><span class="option-text" style="left:63px">1M $ / Year &nbsp;&nbsp; - &nbsp;Gold Power</span>
  </div>
  <div class="option" style="left:0;top:204px;width:847px">
    <span class="radio" style="left:25px"></span><span class="option-text" style="left:63px">3M $ / Year &nbsp;&nbsp; - &nbsp;Platinum Power</span>
  </div>
  <p class="notice"><b>Notic</b> : Lorem ipsum dolor sit amet, consectetuer adipiscing elit, sed diam nonummy nibh euismod tincidunt ut laoreet dolore</p>
</section>

<section class="panel" style="top:564px;height:144px">
  <h2 class="panel-title">Shared Storage Addition</h2>
  <span class="panel-divider" style="top:61px"></span>
  <div class="option" style="left:25px;top:79px"><span class="radio" style="left:0"></span><span class="option-text" style="left:38px">10 Kg</span></div>
  <div class="option is-selected" style="left:177px;top:76px;width:144px;height:42px"><span class="radio" style="left:28px"></span><span class="option-text" style="left:66px">50 Kg</span></div>
  <div class="option" style="left:386px;top:79px"><span class="radio" style="left:0"></span><span class="option-text" style="left:37px">100 Kg</span></div>
  <div class="option" style="left:576px;top:79px"><span class="radio" style="left:0"></span><span class="option-text" style="left:37px">500Kg</span></div>
  <div class="option" style="left:763px;top:79px"><span class="radio" style="left:0"></span><span class="option-text" style="left:36px">1T</span></div>
</section>

<section class="panel" style="top:734px;height:144px">
  <h2 class="panel-title">Additional Tip</h2>
  <span class="panel-divider" style="top:60px"></span>
  <div class="option" style="left:25px;top:79px"><span class="radio" style="left:0"></span><span class="option-text" style="left:38px">15 %</span></div>
  <div class="option is-selected" style="left:177px;top:75px;width:144px;height:41px"><span class="radio" style="left:28px"></span><span class="option-text" style="left:66px">18 %</span></div>
  <div class="option" style="left:386px;top:79px"><span class="radio" style="left:0"></span><span class="option-text" style="left:38px">20 %</span></div>
</section>

<section class="panel" style="top:903px;height:144px">
  <h2 class="panel-title">Elastic Extension</h2>
  <span class="panel-divider" style="top:61px"></span>
  <div class="option" style="left:25px;top:78px"><span class="radio" style="left:0"></span><span class="option-text" style="left:38px">30 %</span></div>
  <div class="option is-selected" style="left:177px;top:75px;width:144px;height:41px"><span class="radio" style="left:28px"></span><span class="option-text" style="left:66px">50 %</span></div>
</section>

<button class="submit" type="submit">SUBMIT
  <svg width="10" height="14" viewBox="0 0 10 14" aria-hidden="true"><path d="M1 1 L9 7 L1 13 Z" fill="#fff"/></svg>
</button>

<footer class="site-footer">© 2017 ENGINE POWER FORM &nbsp;|&nbsp; All rights reserved</footer>
</body>
</html>
```